Bref créative
QDRL Stationary
Professional
Delvonte Ashby
CEO
4815 Marigold Ln
Corvane, NM 87021
dashby@qdrlinc.example
www.QDRLInc.example
My company Logo should be placed on the back of the card.

```html
<!DOCTYPE html>
<html lang="en">
<head>
<meta charset="UTF-8">
<title>QDRL Stationery – Delvonte Ashby</title>
<link href="https://fonts.googleapis.com/css2?family=Roboto:wght@400;700;900&display=swap" rel="stylesheet">
<style>
  :root {
    --backdrop: #ecebe7;
    --green-light: #3fae2a;
    --green-mid: #1f8a1a;
    --green-dark: #0c5e0e;
    --card-white: #ffffff;
    --ink: #2f3132;
    --text-on-green: #ffffff;
    --divider: #c9c9c9;
  }
  html, body {
    margin: 0;
    padding: 0;
    width: 1200px;
    height: 852px;
    overflow: hidden;
    background: var(--backdrop);
    font-family: "Roboto", Arial, sans-serif;
  }
  .canvas {
    position: relative;
    width: 1200px;
    height: 852px;
  }
  .business-card {
    position: absolute;
    width: 540px;
    height: 310px;
    border-radius: 16px;
    overflow: hidden;
    display: flex;
    background: var(--card-white);
    box-shadow: 0 6px 18px rgba(0,0,0,0.18);
  }
  .business-card--first { left: 70px; top: 100px; }
  .business-card--second { left: 590px; top: 440px; }

  .contact-panel {
    width: 52%;
    background: radial-gradient(ellipse at 40% 35%, var(--green-light) 0%, var(--green-mid) 55%, var(--green-dark) 100%);
    color: var(--text-on-green);
    padding: 26px 24px;
    box-sizing: border-box;
    font-size: 12px;
    line-height: 1.45;
    display: flex;
    flex-direction: column;
  }
  .contact-panel--right { text-align: right; border-left: 2px solid var(--divider); }
  .contact-panel--left { border-right: 2px solid var(--divider); }

  .holder-name { font-weight: 700; font-size: 16px; line-height: 1.2; }
  .holder-title { font-size: 12px; margin-bottom: 48px; }
  .address { margin-bottom: 30px; }
  .contact-list { list-style: none; margin: 0; padding: 0; }
  .contact-list li { display: flex; align-items: center; gap: 7px; height: 18px; }
  .contact-panel--right .contact-list li { justify-content: flex-end; }
  .contact-icon { width: 12px; height: 12px; fill: var(--text-on-green); flex: none; }

  .logo-panel {
    flex: 1;
    display: flex;
    align-items: center;
    justify-content: center;
    gap: 12px;
    background: var(--card-white);
  }
  .logo-dot {
    width: 26px;
    height: 26px;
    border-radius: 50%;
    background: var(--green-mid);
  }
  .logo-name {
    font-weight: 900;
    font-size: 52px;
    color: var(--ink);
    letter-spacing: 1px;
  }
</style>
</head>
<body>
<svg width="0" height="0" style="position:absolute">
  <defs>
    <symbol id="icon-phone" viewBox="0 0 24 24"><path d="M6.6 10.8a15 15 0 0 0 6.6 6.6l2.2-2.2c.3-.3.7-.4 1-.2 1.1.4 2.3.6 3.6.6.6 0 1 .4 1 1V20c0 .6-.4 1-1 1A17 17 0 0 1 3 4c0-.6.4-1 1-1h3.5c.6 0 1 .4 1 1 0 1.3.2 2.5.6 3.6.1.3 0 .7-.2 1z"/></symbol>
    <symbol id="icon-mobile" viewBox="0 0 24 24"><path d="M7 1h10a2 2 0 0 1 2 2v18a2 2 0 0 1-2 2H7a2 2 0 0 1-2-2V3a2 2 0 0 1 2-2zm0 3v14h10V4zm5 15.5a1.2 1.2 0 1 0 0 2.4 1.2 1.2 0 0 0 0-2.4z"/></symbol>
    <symbol id="icon-fax" viewBox="0 0 24 24"><path d="M6 2h10l3 3v5H6zM3 11h18a1 1 0 0 1 1 1v9a1 1 0 0 1-1 1H3a1 1 0 0 1-1-1v-9a1 1 0 0 1 1-1zm4 3v2h4v-2zm0 4v2h10v-2z"/></symbol>
    <symbol id="icon-email" viewBox="0 0 24 24"><path d="M12 2a10 10 0 1 0 5 18.7l-1-1.7A8 8 0 1 1 20 12v1.5a1.5 1.5 0 0 1-3 0V7h-2v1a5 5 0 1 0 .5 7A3.5 3.5 0 0 0 22 13.5V12A10 10 0 0 0 12 2zm0 13a3 3 0 1 1 0-6 3 3 0 0 1 0 6z"/></symbol>
  </defs>
</svg>

<main class="canvas">
  <article class="business-card business-card--first">
    <section class="contact-panel contact-panel--left">
      <div class="holder-name">Delvonte Ashby</div>
      <div class="holder-title">CEO</div>
      <div class="address">4815 Marigold Ln<br>Corvane, NM 87021</div>
      <ul class="contact-list">
        <li><svg class="contact-icon"><use href="#icon-phone"/></svg>(T) 877-555-0142</li>
        <li><svg class="contact-icon"><use href="#icon-mobile"/></svg>505-555-0187</li>
        <li><svg class="contact-icon"><use href="#icon-fax"/></svg>877-555-0142</li>
        <li><svg class="contact-icon"><use href="#icon-email"/></svg>dashby@qdrlinc.example</li>
      </ul>
    </section>
    <section class="logo-panel">
      <span class="logo-dot"></span>
      <span class="logo-name">QDRL</span>
    </section>
  </article>

  <article class="business-card business-card--second">
    <section class="logo-panel">
      <span class="logo-dot"></span>
      <span class="logo-name">QDRL</span>
    </section>
    <section class="contact-panel contact-panel--right">
      <div class="holder-name">Delvonte Ashby</div>
      <div class="holder-title">CEO</div>
      <div class="address">4815 Marigold Ln<br>Corvane, NM 87021</div>
      <ul class="contact-list">
        <li>(T) 877-555-0142<svg class="contact-icon"><use href="#icon-phone"/></svg></li>
        <li>505-555-0187<svg class="contact-icon"><use href="#icon-mobile"/></svg></li>
        <li>877-555-0142<svg class="contact-icon"><use href="#icon-fax"/></svg></li>
        <li>dashby@qdrlinc.example<svg class="contact-icon"><use href="#icon-email"/></svg></li>
      </ul>
    </section>
  </article>
</main>
</body>
</html>
```